Website Design for WeselneKarety.pl – Luxury Wedding Car Rental with Chauffeur

We are looking for a talented designer to create a modern, elegant, and fully responsive website for our new brand – WeselnyKarety.pl. We are a premium car rental platform in Poland, offering luxury and exotic vehicles exclusively for weddings. All cars come with a professional chauffeur, ensuring a high-end, stress-free, and stylish experience.
Website Purpose:
The website should present our offering in a luxurious, clear, and inspiring way. It must build trust, highlight the prestige of our brand, and encourage inquiries. Our target audience includes engaged couples, wedding planners, and clients seeking a truly exceptional vehicle for their special day.
Design Requirements:
Style: modern, elegant, minimalist
Color palette: white, black, gold, optionally silver – refined and luxurious
Typography: clean, modern, high-end
Layout: clear, intuitive, with large car images and well-defined sections
Fully responsive (desktop, tablet, mobile)
Bilingual layout (Polish/English) must be considered
Pages to Design:
Homepage
About Us
Fleet Overview
Individual Car Pages
Services (Weddings, Photo Shoots, Film Rentals)
Why Us / Unique Selling Points
Contact
FAQ
Inspiration:
Luxury automotive brands (e.g. Varnell-Dorne, Corwick, Elsby Havard)
High-end wedding websites
Minimalist layouts with large visuals and elegant typography
Additional Notes:
The design should evoke the emotions of a wedding day – elegance, uniqueness, style, and class. Please avoid flashy colors, excessive graphic effects, or overly decorative elements. Subtlety, prestige, and sophistication are key.

```html
<!DOCTYPE html>
<html lang="en">
<head>
<meta charset="utf-8">
<title>About Us – WeselneKarety.pl</title>
<link href="https://fonts.googleapis.com/css2?family=Quicksand:wght@300;400;500&display=swap" rel="stylesheet">
<style>
  :root {
    --navy: #16202e;
    --navy-light: #1c2838;
    --gold: #d7b85a;
    --ink: #2b2f36;
    --body-text: #3f4a5a;
    --white: #ffffff;
    --footer-bg: #1e1e1e;
    --footer-text: #b9b9b9;
    --footer-head: #d9d9d9;
    --footer-line: #3a3a3a;
  }
  * { margin: 0; padding: 0; box-sizing: border-box; }
  html, body {
    width: 1200px; height: 2709px; overflow: hidden;
    background: var(--white);
    font-family: "Quicksand", sans-serif;
    color: var(--body-text);
  }
  .page { position: relative; width: 1200px; height: 2709px; }
  .abs { position: absolute; }

  .hero {
    left: 0; top: 0; width: 1200px; height: 433px;
    background: linear-gradient(135deg, var(--navy) 0%, var(--navy-light) 60%, var(--navy) 100%);
  }
  .brand { display: flex; align-items: center; gap: 8px; color: var(--gold); font-weight: 500; font-size: 17px; letter-spacing: 0.5px; }
  .brand-dot { width: 12px; height: 12px; border-radius: 50%; border: 1.5px solid var(--gold); }
  .site-brand { left: 66px; top: 40px; }
  .nav { top: 42px; display: flex; align-items: center; gap: 8px; color: #c9d0da; font-size: 13.5px; letter-spacing: 0.6px; }
  .nav-find { left: 926px; }
  .nav-menu { left: 1067px; }
  .page-title {
    left: 0; width: 1200px; top: 187px; text-align: center;
    color: #d8dde4; font-weight: 300; font-size: 31px; letter-spacing: 9px;
  }

  .photo-car-white { left: 66px; top: 299px; width: 534px; height: 399px; background: linear-gradient(120deg, #f1f1f1 0%, #d8d8d8 45%, #6a6a6a 80%, #2c2c2c 100%); }

  .legacy-title { left: 628px; top: 536px; font-size: 35px; font-weight: 400; color: var(--ink); letter-spacing: 0.5px; }
  .legacy-text { left: 628px; width: 482px; font-size: 13.1px; line-height: 22.5px; font-weight: 400; color: var(--body-text); }
  .legacy-text.first { top: 592px; }
  .legacy-text.second { top: 727px; }

  .section-title {
    left: 0; width: 1200px; top: 925px; text-align: center;
    font-size: 25px; font-weight: 400; letter-spacing: 3.5px; color: var(--ink);
  }

  .feature-title { font-size: 20.5px; font-weight: 400; letter-spacing: 3px; color: var(--ink); }
  .feature-text { font-size: 13.6px; line-height: 22.5px; color: var(--body-text); margin-top: 12px; letter-spacing: 0.2px; }
  .feature-quality { left: 109px; top: 1151px; }
  .feature-quality .feature-text { width: 400px; }
  .feature-personal { left: 643px; top: 1584px; }
  .feature-personal .feature-text { width: 390px; }
  .feature-peace { left: 109px; top: 2016px; }
  .feature-peace .feature-text { width: 355px; }

  .photo-interior { left: 600px; top: 1015px; width: 533px; height: 350px; background: linear-gradient(135deg, #5a5a5a 0%, #1e1e1e 50%, #3b3b3b 100%); }
  .photo-bride { left: 67px; top: 1447px; width: 533px; height: 350px; background: linear-gradient(90deg, #2a2a2a 0%, #e9e4dc 30%, #d8cfc2 55%, #5a4030 80%, #1a1a1a 100%); }
  .photo-couple { left: 600px; top: 1880px; width: 534px; height: 350px; background: linear-gradient(180deg, #7c8a70 0%, #4b5448 40%, #1d2230 70%, #6a6560 100%); }

  .footer { left: 0; top: 2317px; width: 1200px; height: 392px; background: var(--footer-bg); color: var(--footer-text); }
  .footer-brand { left: 66px; top: 37px; }
  .tagline { left: 66px; top: 98px; font-size: 13.5px; color: var(--footer-head); letter-spacing: 0.3px; }
  .tagline-sub { left: 66px; top: 120px; font-size: 10px; }
  .follow { left: 66px; top: 160px; font-size: 13.5px; color: var(--footer-head); letter-spacing: 0.3px; }
  .follow-links { left: 66px; top: 182px; font-size: 10px; display: flex; gap: 8px; }
  .col-title { font-size: 13.5px; color: var(--footer-head); letter-spacing: 0.3px; }
  .col-list { list-style: none; margin-top: 17px; font-size: 10px; }
  .col-list li { height: 25px; }
  .col-explore { left: 455px; top: 39px; }
  .col-offer { left: 627px; top: 39px; }
  .col-contact { left: 868px; top: 39px; font-size: 10px; line-height: 16px; }
  .col-contact .col-title { margin-bottom: 17px; }
  .col-contact strong { font-weight: 500; color: #d0d0d0; }
  .col-contact .block { margin-bottom: 21px; }
  .footer-rule { left: 66px; top: 333px; width: 1067px; height: 1px; background: var(--footer-line); }
  .copyright { left: 66px; top: 350px; font-size: 10px; }
  .legal { right: 67px; top: 350px; font-size: 10px; display: flex; gap: 16px; }
</style>
</head>
<body>
<div class="page">

  <header class="abs hero">
    <div class="abs brand site-brand"><span class="brand-dot"></span>WeselneKarety</div>
    <div class="abs nav nav-find">
      <svg width="14" height="14" viewBox="0 0 14 14" fill="none" stroke="#c9d0da" stroke-width="1.3"><circle cx="6" cy="6" r="4.5"/><line x1="9.3" y1="9.3" x2="13" y2="13"/></svg>
      FIND A CAR
    </div>
    <div class="abs nav nav-menu">
      <svg width="16" height="12" viewBox="0 0 16 12" stroke="#c9d0da" stroke-width="1.2"><line x1="0" y1="1" x2="10" y2="1"/><line x1="0" y1="6" x2="13" y2="6"/><line x1="0" y1="11" x2="16" y2="11"/></svg>
      MENU
    </div>
    <h1 class="abs page-title">ABOUT US</h1>
  </header>

  <div class="abs photo-car-white" role="img" aria-label="Close-up of a white luxury car front with headlight and alloy wheel"></div>

  <h2 class="abs legacy-title">A LEGACY OF LUXURY</h2>
  <p class="abs legacy-text first">Founded on the belief that every couple deserves an extraordinary wedding day, we have dedicated ourselves to curating the finest collection of luxury vehicles and providing unparalleled service. Our passion for excellence and attention to detail has made us the trusted choice for discerning couples who settle for nothing less than perfection.</p>
  <p class="abs legacy-text second">With years of experience in luxury transportation and wedding services, we understand that your wedding day is not just an event—it's the beginning of your forever story. Every vehicle in our fleet and every member of our team is committed to ensuring this chapter begins with elegance, sophistication, and unforgettable memories.</p>

  <h2 class="abs section-title">OUR COMMITMENT</h2>

  <div class="abs feature-quality">
    <h3 class="feature-title">UNCOMPROMISING QUALITY</h3>
    <p class="feature-text">Every vehicle undergoes rigorous maintenance and detailed preparation before your special day.</p>
  </div>
  <div class="abs photo-interior" role="img" aria-label="Black leather interior of a sports car with steering wheel and gear shifter"></div>

  <div class="abs photo-bride" role="img" aria-label="Bride in white dress seated in a classic black car with wooden trim"></div>
  <div class="abs feature-personal">
    <h3 class="feature-title">PERSONALIZED SERVICE</h3>
    <p class="feature-text">No two weddings are alike, and neither is our approach to serving each couple's unique vision.</p>
  </div>

  <div class="abs feature-peace">
    <h3 class="feature-title">PEACE OF MIND</h3>
    <p class="feature-text">Comprehensive insurance, backup vehicles, and 24/7 support ensure your day proceeds flawlessly.</p>
  </div>
  <div class="abs photo-couple" role="img" aria-label="Groom stepping out of a vintage black car toward the bride in a garden setting"></div>

  <footer class="abs footer">
    <div class="abs brand footer-brand"><span class="brand-dot"></span>WeselneKarety</div>
    <div class="abs tagline">CREATING PERFECT BEGINNINGS</div>
    <div class="abs tagline-sub">Wedding Transportation | Bridal Car Service | Luxury Chauffeur</div>
    <div class="abs follow">FOLLOW US</div>
    <div class="abs follow-links"><span>Snapfolio</span><span>Friendbook</span><span>ViewTube</span></div>

    <nav class="abs col-explore">
      <div class="col-title">EXPLORE</div>
      <ul class="col-list">
        <li>Our Fleet</li><li>Wedding Services</li><li>Gallery</li><li>Testimonials</li>
        <li>About Us</li><li>Pricing &amp; Packages</li><li>Wedding Planning Guide</li><li>FAQ</li>
      </ul>
    </nav>
    <nav class="abs col-offer">
      <div class="col-title">OUR OFFERINGS</div>
      <ul class="col-list">
        <li>Classic Luxury Cars</li><li>Modern Premium Vehicles</li><li>Vintage Collection</li><li>Chauffeur Services</li>
        <li>Wedding Coordination</li><li>Photography Support</li><li>Custom Packages</li><li>Event Transportation</li>
      </ul>
    </nav>
    <div class="abs col-contact">
      <div class="col-title">GET IN TOUCH</div>
      <div class="block">
        <strong>Contact Information:</strong><br>
        Phone: +48 12 340 18 27<br>
        Email: rezerwacje@weselnekarety.pl<br>
        Address: 12 Aleja Lipowa, Kraków 30-001
      </div>
      <div class="block">
        <strong>Business Hours:</strong><br>
        Monday - Friday: 9:00 AM - 7:00 PM<br>
        Saturday: 10:00 AM - 4:00 PM<br>
        Sunday: By Appointment Only
      </div>
      <div class="block">
        <strong>Emergency Contact:</strong><br>
        24/7 Wedding Day Support: +48 600 214 905
      </div>
    </div>

    <div class="abs footer-rule"></div>
    <div class="abs copyright">Copyright: © 2024 WeselnyKarety.pl. All Rights Reserved.</div>
    <div class="abs legal"><span>Privacy Policy</span><span>Terms of Service</span><span>Cancellation Policy</span><span>Insurance Information</span></div>
  </footer>

</div>
</body>
</html>
```